International gym review site. Needs a full website frontend (mobile + desktop) designing and a logo

Our UK based business 'LiftHarbor' is launching its international review website for independent and hotel gyms. Our website will be a fresh, funky and clean version of Wanderquill but for gyms.
We require the designs in sketch, psd, illustrator

We would like to see clean designs that incorporate gym style icons. We also require our logo designing which will need to complement the design of the site. We have included wireframes of how we envisage the site coming together. However, we are very flexible on this and have nothing set in stone.

We would like the designs to mobile first focused with desktop experince being the latter (although we have wireframed for desktop - we are very open to ideas and suggestions)

Please find below a number of websites that we like and have found inspiration from:

- https://www.bookvane.example/uk/
- chatterloom.example
- Map is cool on here https://bigroster.bypilotcraft.example/
- Looks cool like nest n'go (listing section could be smaller) -https://tintforge.example/demos/themes/?product=rowable
- Like this but needs to be more compact https://rowkit-demos.brimfold.example/rentals/listing/private-bedroom-w-bathroom/
- Like the homepage of this one https://rankhop.venmora.example/
- https://www.paddlo.example.co.uk/hotels - looks clean, like the layout of this especially the hotel section
- https://www.paddlo.example.co.uk/Barcelona-Hotels.48213.hotel.ksp - the good to know section is good
- https://chipwire.example/2017/10/20/flickcast-unveils-a-suite-of-new-tools-to-help-creators-grow-their-channels-and-make-money/
- https://www.quietlodging.example/
- https://www.wheelmarket.example.co.uk

Target Market(s)

Fitness users and hotel goers who want to use a gym. Generally affluent aged 20-50years old of multi-nationalities

Industry/Entity Type

Fitness

Logo Text

LiftHarbor (optional)

Number of Pages Required

5+ page

Colors

Designer to choose colors to be used in the design.

Requirements
Must have
• Clean, flat minimal, pleasing on the eye.
• Bright / colourful
• Clean fonts (no specific font picked, will leave colour palette and fonts to the designer)
Should not have
• Cluttered and disorganised feel.
• Dark and dreary.

```html
<!DOCTYPE html>
<html lang="en">
<head>
<meta charset="utf-8">
<title>LiftHarbor — Find Hotel & Independent Gyms</title>
<link href="https://fonts.googleapis.com/css2?family=Montserrat:wght@400;600;700;800&family=Open+Sans:wght@400;600&display=swap" rel="stylesheet">
<style>
:root{
  --yellow:#f7c10c;
  --black:#111111;
  --ink:#222222;
  --grey:#8a8a8a;
  --light:#f2f2f2;
  --white:#ffffff;
  --dark-photo-a:#3a3a3a;
  --dark-photo-b:#121212;
}
*{box-sizing:border-box;margin:0;padding:0}
html,body{width:682px;height:1200px;overflow:hidden;background:var(--white)}
body{font-family:"Open Sans",Arial,sans-serif;color:var(--ink);position:relative}
.page{position:relative;width:682px;height:1200px;overflow:hidden}

/* top bar */
.topbar{height:18px;background:var(--black);color:#ddd;font-size:7px;display:flex;align-items:center;justify-content:space-between;padding:0 98px}
.topbar span b{color:var(--yellow);font-weight:600}

/* header */
.header{height:32px;display:flex;align-items:center;justify-content:space-between;padding:0 98px;background:var(--white)}
.brand{display:flex;align-items:center;gap:5px;font-family:"Montserrat",sans-serif;font-weight:700;font-size:10px;color:var(--ink)}
.brand-dot{width:14px;height:14px;border-radius:50%;background:var(--yellow)}
.nav{display:flex;align-items:center;gap:16px;font-family:"Montserrat",sans-serif;font-size:6.5px;font-weight:600;color:var(--ink)}
.nav .active{color:var(--yellow)}
.nav .search{width:16px;height:16px;border:1.5px solid var(--ink);border-radius:50%;display:flex;align-items:center;justify-content:center}

/* hero */
.hero{position:relative;height:286px}
.hero-photo{position:absolute;inset:0;background:linear-gradient(100deg,#5a5450 0%,#2a2624 40%,#3d3632 70%,#1c1a19 100%)}
.hero-content{position:absolute;left:0;right:0;top:82px;text-align:center;color:var(--white)}
.hero-title{font-family:"Montserrat",sans-serif;font-weight:700;font-size:24px;letter-spacing:.5px}
.hero-place{font-size:10px;margin-top:4px}
.hero-stars{margin-top:6px;display:flex;justify-content:center;gap:3px}
.hero-rating{font-size:6px;margin-top:3px;color:#ccc}
.hero-actions{margin-top:16px;display:flex;justify-content:center;gap:8px}
.btn{font-family:"Montserrat",sans-serif;font-size:6.5px;font-weight:700;padding:6px 12px;text-transform:uppercase}
.btn-yellow{background:var(--yellow);color:var(--black)}
.btn-outline{border:1px solid var(--white);color:var(--white)}
.hero-arrow{position:absolute;top:124px;width:22px;height:34px;display:flex;align-items:center;justify-content:center}
.hero-arrow.prev{left:0;background:rgba(80,80,80,.85)}
.hero-arrow.next{right:0;background:var(--yellow)}

/* find bar */
.findbar{height:32px;background:var(--black);display:flex;align-items:center;padding:0 98px;gap:10px;color:var(--white);font-size:7px}
.findbar .label{font-family:"Montserrat",sans-serif;font-weight:700;font-size:8px;margin-right:14px}
.findbar .field{display:flex;align-items:center;gap:6px}
.findbar .input{background:var(--white);color:var(--grey);font-size:6px;padding:4px 6px;width:94px;height:14px}
.findbar .go{margin-left:auto;background:var(--yellow);color:var(--black);font-weight:700;font-size:6.5px;padding:4px 10px}

/* listing sections */
.listing{position:relative;height:246px;background:var(--white)}
.section-title{font-family:"Montserrat",sans-serif;font-weight:700;font-size:15px;text-align:center;padding-top:38px;color:var(--ink)}
.section-title em{font-style:normal;color:var(--yellow)}
.cards{position:absolute;top:80px;left:0;right:0;display:flex;justify-content:center;align-items:center;gap:8px}
.card{width:86px;background:var(--white);box-shadow:0 1px 3px rgba(0,0,0,.18)}
.card .photo{height:52px;background:linear-gradient(135deg,#bfbfbf,#7d7d7d)}
.card .body{padding:4px 5px 5px}
.card .name{font-size:5.5px;font-weight:600}
.card .meta{font-size:4.5px;color:var(--grey);margin-top:1px}
.card .stars{margin-top:3px;display:flex;gap:1px}
.card.fade{opacity:.55}
.card.featured{width:104px;background:var(--black);border:2px solid var(--yellow);color:var(--white)}
.card.featured .photo{height:72px;background:linear-gradient(135deg,#6a6a6a,#2b2b2b)}
.card.featured .name{font-size:6.5px}
.card.featured .meta{color:#bbb}

/* gym types */
.types{position:relative;height:205px;margin-top:4px}
.types-photo{position:absolute;inset:0;background:radial-gradient(ellipse at 40% 40%,#4a4a4a 0%,#262626 55%,#141414 100%)}
.types-head{position:relative;text-align:center;color:var(--white);padding-top:48px}
.types-head h3{font-family:"Montserrat",sans-serif;font-weight:700;font-size:9px}
.types-head p{font-size:5.5px;color:#ccc;margin-top:3px}
.type-list{position:relative;display:flex;justify-content:center;gap:22px;margin-top:16px}
.type{width:56px;text-align:center;color:var(--white);font-size:6.5px}
.type .ring{width:52px;height:52px;border-radius:50%;background:var(--white);margin:0 auto 7px;display:flex;align-items:center;justify-content:center;border:3px solid #d8d8d8}

/* footer */
.footer{position:absolute;left:0;right:0;top:1082px;height:118px;background:var(--black);color:#cfcfcf;display:flex;gap:22px;padding:14px 98px 0}
.footer h4{font-family:"Montserrat",sans-serif;font-size:8px;color:var(--white);margin-bottom:7px}
.footer p{font-size:4.8px;line-height:1.45}
.f-col{width:104px}
.news-input{display:flex;margin-top:7px}
.news-input span{flex:1;background:var(--white);height:12px}
.news-input b{background:var(--yellow);width:24px;height:12px}
.news-item{display:flex;gap:5px;margin-bottom:6px}
.news-item i{width:22px;height:16px;background:linear-gradient(135deg,#777,#444);flex:none}
.tags{display:flex;flex-wrap:wrap;gap:3px}
.tags span{border:1px solid #666;font-size:4.5px;padding:2px 4px}
.socials{display:flex;gap:4px;margin-top:6px}
.socials i{width:9px;height:9px;border-radius:50%;background:#555}
</style>
</head>
<body>
<div class="page">

  <div class="topbar">
    <span>Customer Login</span>
    <span>Call Member <b>Phone</b>: +44 20 7946 0321</span>
  </div>

  <header class="header">
    <div class="brand"><span class="brand-dot"></span>LiftHarbor</div>
    <nav class="nav">
      <span class="active">HOME</span><span>LIST OF GYM</span><span>GYM FILE</span><span>BLOG</span><span>CONTACT US</span>
      <span class="search"><svg width="7" height="7" viewBox="0 0 10 10"><circle cx="4" cy="4" r="3" fill="none" stroke="#222" stroke-width="1.5"/><line x1="6.3" y1="6.3" x2="9" y2="9" stroke="#222" stroke-width="1.5"/></svg></span>
    </nav>
  </header>

  <section class="hero">
    <div class="hero-photo" role="img" aria-label="Athletes training with suspension straps in a gym"></div>
    <div class="hero-content">
      <div class="hero-title">GET SHAPED GYM</div>
      <div class="hero-place">Toronto, Canada</div>
      <div class="hero-stars">
        <svg width="70" height="12" viewBox="0 0 70 12" fill="#f7c10c"><g id="s"><polygon points="6,0 7.8,4 12,4.4 8.8,7.2 9.8,11.5 6,9.2 2.2,11.5 3.2,7.2 0,4.4 4.2,4"/></g><use href="#s" x="14"/><use href="#s" x="28"/><use href="#s" x="42"/><use href="#s" x="56"/></svg>
      </div>
      <div class="hero-rating">5 REVIEWS</div>
      <div class="hero-actions"><span class="btn btn-yellow">View on the map</span><span class="btn btn-outline">More info</span></div>
    </div>
    <div class="hero-arrow prev"><svg width="7" height="10" viewBox="0 0 7 10"><polyline points="6,1 2,5 6,9" fill="none" stroke="#fff" stroke-width="1.6"/></svg></div>
    <div class="hero-arrow next"><svg width="7" height="10" viewBox="0 0 7 10"><polyline points="1,1 5,5 1,9" fill="none" stroke="#111" stroke-width="1.6"/></svg></div>
  </section>

  <div class="findbar">
    <span class="label">FIND GYM</span>
    <span class="field">Where <span class="input">Name or City</span></span>
    <span class="field" style="margin-left:10px">Type <span class="input">Hotel Gym</span></span>
    <span class="go">Search</span>
  </div>

  <section class="listing">
    <h2 class="section-title">HOTEL <em>GYM</em></h2>
    <div class="cards">
      <div class="card fade"><div class="photo" role="img" aria-label="Gym interior"></div><div class="body"><div class="name">Highlights Gym</div><div class="meta">12 Harbour Street</div></div></div>
      <div class="card"><div class="photo" role="img" aria-label="Hotel gym room"></div><div class="body"><div class="name">Highlights Gym</div><div class="meta">12 Harbour Street</div></div></div>
      <div class="card featured"><div class="photo" role="img" aria-label="Athlete training with battle ropes"></div><div class="body"><div class="name">Get Healthy Gym</div><div class="meta">London, United Kingdom</div><div class="stars"><svg width="34" height="6" viewBox="0 0 70 12" fill="#f7c10c"><use href="#s"/><use href="#s" x="14"/><use href="#s" x="28"/><use href="#s" x="42"/><use href="#s" x="56"/></svg></div></div></div>
      <div class="card"><div class="photo" role="img" aria-label="Group fitness class"></div><div class="body"><div class="name">Highlights Gym</div><div class="meta">12 Harbour Street</div><div class="stars"><svg width="30" height="5" viewBox="0 0 70 12" fill="#f7c10c"><use href="#s"/><use href="#s" x="14"/><use href="#s" x="28"/><use href="#s" x="42"/><use href="#s" x="56"/></svg></div></div></div>
      <div class="card"><div class="photo" role="img" aria-label="Weightlifting area"></div><div class="body"><div class="name">Independent Gym</div><div class="meta">12 Harbour Street</div><div class="stars"><svg width="30" height="5" viewBox="0 0 70 12" fill="#f7c10c"><use href="#s"/><use href="#s" x="14"/><use href="#s" x="28"/><use href="#s" x="42"/><use href="#s" x="56"/></svg></div></div></div>
      <div class="card fade"><div class="photo" role="img" aria-label="Barbell training"></div><div class="body"><div class="name">Highlights Gym</div><div class="meta">12 Harbour Street</div></div></div>
    </div>
  </section>

  <section class="types">
    <div class="types-photo" role="img" aria-label="Barbell plates on a dark gym floor"></div>
    <div class="types-head">
      <h3>GYM TYPE</h3>
      <p>Choose the type of gym that suits your training</p>
    </div>
    <div class="type-list">
      <div class="type"><div class="ring"><svg width="22" height="24" viewBox="0 0 22 24" fill="#222"><rect x="4" y="2" width="14" height="22"/><g fill="#fff"><rect x="7" y="5" width="3" height="3"/><rect x="12" y="5" width="3" height="3"/><rect x="7" y="11" width="3" height="3"/><rect x="12" y="11" width="3" height="3"/><rect x="9" y="18" width="4" height="6"/></g></svg></div>Hotel</div>
      <div class="type"><div class="ring"><svg width="26" height="24" viewBox="0 0 26 24" fill="#222"><rect x="1" y="8" width="10" height="16"/><rect x="12" y="1" width="13" height="23"/><g fill="#fff"><rect x="3" y="11" width="2" height="2"/><rect x="7" y="11" width="2" height="2"/><rect x="3" y="16" width="2" height="2"/><rect x="7" y="16" width="2" height="2"/><rect x="15" y="4" width="3" height="3"/><rect x="20" y="4" width="3" height="3"/><rect x="15" y="10" width="3" height="3"/><rect x="20" y="10" width="3" height="3"/><rect x="15" y="16" width="3" height="3"/><rect x="20" y="16" width="3" height="3"/></g></svg></div>Apartment</div>
      <div class="type"><div class="ring"><svg width="28" height="14" viewBox="0 0 28 14" fill="#222"><rect x="1" y="3" width="3" height="8"/><rect x="4" y="0" width="4" height="14"/><rect x="8" y="6" width="12" height="2"/><rect x="20" y="0" width="4" height="14"/><rect x="24" y="3" width="3" height="8"/></svg></div>Independent</div>
      <div class="type"><div class="ring"><svg width="28" height="20" viewBox="0 0 28 20" fill="none" stroke="#222" stroke-width="2"><circle cx="6" cy="14" r="5"/><circle cx="22" cy="14" r="5"/><polyline points="6,14 11,5 19,5 22,14"/><polyline points="11,5 14,14 19,5"/><line x1="9" y1="2" x2="13" y2="2"/></svg></div>Cycling</div>
      <div class="type"><div class="ring"><svg width="24" height="22" viewBox="0 0 24 22" fill="#222"><rect x="2" y="8" width="20" height="6" rx="2"/><polygon points="10,14 7,22 10,22 12,16 14,22 17,22 14,14"/></svg></div>Defense</div>
      <div class="type"><div class="ring"><svg width="20" height="24" viewBox="0 0 20 24" fill="#222"><path d="M6 8 a4 4 0 0 1 8 0 h-2 a2 2 0 0 0 -4 0z"/><path d="M3 10 h14 l2 10 q0 4 -4 4 h-10 q-4 0 -4 -4z"/></svg></div>Body Building</div>
    </div>
  </section>

  <section class="listing" style="margin-top:18px">
    <h2 class="section-title">INDEPENDENT <em>GYM</em></h2>
    <div class="cards">
      <div class="card fade"><div class="photo" role="img" aria-label="Gym interior"></div><div class="body"><div class="name">Highlights Gym</div><div class="meta">12 Harbour Street</div></div></div>
      <div class="card"><div class="photo" role="img" aria-label="Independent gym floor"></div><div class="body"><div class="name">Highlights Gym</div><div class="meta">12 Harbour Street</div></div></div>
      <div class="card featured"><div class="photo" role="img" aria-label="Athlete training with battle ropes"></div><div class="body"><div class="name">Get Healthy Gym</div><div class="meta">London, United Kingdom</div><div class="stars"><svg width="34" height="6" viewBox="0 0 70 12" fill="#f7c10c"><use href="#s"/><use href="#s" x="14"/><use href="#s" x="28"/><use href="#s" x="42"/><use href="#s" x="56"/></svg></div></div></div>
      <div class="card"><div class="photo" role="img" aria-label="Group fitness class"></div><div class="body"><div class="name">Highlights Gym</div><div class="meta">12 Harbour Street</div><div class="stars"><svg width="30" height="5" viewBox="0 0 70 12" fill="#f7c10c"><use href="#s"/><use href="#s" x="14"/><use href="#s" x="28"/><use href="#s" x="42"/><use href="#s" x="56"/></svg></div></div></div>
      <div class="card"><div class="photo" role="img" aria-label="Weightlifting area"></div><div class="body"><div class="name">Highlights Gym</div><div class="meta">12 Harbour Street</div><div class="stars"><svg width="30" height="5" viewBox="0 0 70 12" fill="#f7c10c"><use href="#s"/><use href="#s" x="14"/><use href="#s" x="28"/><use href="#s" x="42"/><use href="#s" x="56"/></svg></div></div></div>
      <div class="card fade"><div class="photo" role="img" aria-label="Barbell training"></div><div class="body"><div class="name">Highlights Gym</div><div class="meta">12 Harbour Street</div></div></div>
    </div>
  </section>

  <footer class="footer">
    <div class="f-col">
      <h4>Newsletter</h4>
      <p>Sign up for gym reviews, new listings and training tips from hotels and studios around the world.</p>
      <div class="news-input"><span></span><b></b></div>
    </div>
    <div class="f-col">
      <h4>Latest News</h4>
      <div class="news-item"><i role="img" aria-label="News thumbnail"></i><p>Best hotel gyms to visit this summer season</p></div>
      <div class="news-item"><i role="img" aria-label="News thumbnail"></i><p>Ten quick workouts for busy travellers</p></div>
    </div>
    <div class="f-col">
      <h4>Tags</h4>
      <div class="tags"><span>Hotel Gym</span><span>Cycling</span><span>Yoga</span><span>Boxing</span><span>Weights</span><span>Cardio</span><span>Studio</span></div>
    </div>
    <div class="f-col">
      <h4>Address</h4>
      <p>14 Quayside Row, Bristol BS1 4QA<br>+44 20 7946 0321<br>hello@liftharbor.example</p>
      <div class="socials"><i></i><i></i><i></i><i></i><i></i></div>
    </div>
  </footer>

</div>
</body>
</html>
```